Newsletter template

I am looking for 2 newsletter templates. My website is in Wordpress and I want to use in mailchimp for lists.

One newsletter is for local clients of design remodeling firm to be sent monthly

Second newsletter is for web store offerings to be sent weekly.

Target Market(s)

Luxury home and leisure

Industry/Entity Type

Store

Requirements
Must have
• Use logos and colors to seamlessly integrate with website,

```html
<!DOCTYPE html>
<html lang="en">
<head>
<meta charset="utf-8">
<title>Newsletter – Product Offer</title>
<link rel="stylesheet" href="https://fonts.googleapis.com/css2?family=Arimo:wght@400;700&display=swap">
<style>
  :root {
    --bg: #ffffff;
    --text: #6f6f6f;
    --heading: #3a3a3a;
    --accent: #22aecd;
    --link: #1d9ec4;
    --badge: #d6e000;
    --btn-grey: #7a7a7a;
    --rule-dark: #444444;
    --rule-light: #e4e4e4;
    --bottom-line: #9a9a9a;
    --social-1: #3aa6d6;
    --social-2: #3d5f9e;
    --social-3: #5aa447;
    --social-4: #c8333a;
  }
  * { margin: 0; padding: 0; box-sizing: border-box; }
  html, body {
    width: 1200px; height: 736px; overflow: hidden;
    background: var(--bg);
    font-family: "Arimo", Arial, sans-serif;
  }
  .newsletter { position: relative; width: 1200px; height: 736px; }

  .divider {
    position: absolute; left: 35px; width: 1135px; height: 10px;
    background: radial-gradient(ellipse at center, var(--rule-light) 0%, rgba(228,228,228,0.6) 55%, rgba(255,255,255,0) 100%);
  }
  .divider--top { top: 22px; }
  .divider--bottom { top: 438px; }

  .product__image {
    position: absolute; left: 53px; top: 112px; width: 337px; height: 290px;
    background: radial-gradient(ellipse at 50% 55%, #e9e9e9 0%, #f3f3f3 45%, #ffffff 75%);
  }
  .product__badge {
    position: absolute; left: 424px; top: 92px; height: 41px; padding: 0 13px;
    background: var(--badge); color: #fff; font-weight: 700; font-size: 18px;
    line-height: 41px; letter-spacing: 0.2px;
  }
  .product__title {
    position: absolute; left: 423px; top: 154px;
    font-size: 35px; font-weight: 400; color: var(--accent); line-height: 1.2;
  }
  .product__text {
    position: absolute; left: 424px; top: 220px; width: 740px;
    font-size: 20.5px; line-height: 39px; color: var(--text);
  }
  .product__actions { position: absolute; left: 424px; top: 315px; display: flex; gap: 11px; }
  .button {
    display: block; height: 38px; line-height: 38px; text-align: center;
    color: #fff; font-weight: 700; font-size: 17px; text-decoration: none;
    box-shadow: 0 2px 0 rgba(0,0,0,0.12);
  }
  .button--view { width: 113px; background: var(--btn-grey); }
  .button--buy { width: 115px; background: var(--accent); }

  .footer__address, .footer__web {
    position: absolute; top: 503px; font-size: 20.5px; line-height: 34px;
  }
  .footer__address { left: 43px; color: var(--text); }
  .footer__web { left: 427px; }
  .footer__web a { color: var(--link); text-decoration: none; display: block; }
  .footer__social { position: absolute; left: 925px; top: 511px; }
  .footer__rule {
    position: absolute; left: 43px; top: 607px; width: 349px; height: 8px;
    background: var(--rule-dark);
  }
  .footer__company {
    position: absolute; left: 43px; top: 647px;
    font-size: 28px; font-weight: 700; color: var(--heading);
  }
  .page-end {
    position: absolute; left: 0; top: 727px; width: 1200px; height: 2px;
    background: var(--bottom-line);
  }
</style>
</head>
<body>
<div class="newsletter">
  <div class="divider divider--top"></div>

  <section class="product">
    <div class="product__image" role="img" aria-label="Product photo: stacked white boxes with a book standing on top"></div>
    <div class="product__badge">SPECIAL PRICE: 8$</div>
    <h2 class="product__title">Vivamus Vivamus</h2>
    <p class="product__text">Donec porttitor quam vel purus venenatis rutrum. Nullam quam nibh, congue sed aliquet posuere, aliquam non lacus. Maecenas nec luctus neque...</p>
    <div class="product__actions">
      <a class="button button--view" href="#">VIEW</a>
      <a class="button button--buy" href="#">BUY</a>
    </div>
  </section>

  <div class="divider divider--bottom"></div>

  <footer class="footer">
    <div class="footer__address">
      <p>Company adress, City, State</p>
      <p>Phone: 1-800-0000-000</p>
    </div>
    <div class="footer__web">
      <a href="#">info@companywebsite.com</a>
      <a href="#">companywebsite.com</a>
    </div>
    <svg class="footer__social" width="240" height="46" viewBox="0 0 240 46" role="img" aria-label="Social media links">
      <circle cx="23" cy="22" r="21" fill="var(--social-1)"/>
      <circle cx="83" cy="22" r="21" fill="var(--social-2)"/>
      <circle cx="143" cy="22" r="21" fill="var(--social-3)"/>
      <circle cx="204" cy="22" r="21" fill="var(--social-4)"/>
    </svg>
    <div class="footer__rule"></div>
    <p class="footer__company">Company name Ltd.</p>
  </footer>

  <div class="page-end"></div>
</div>
</body>
</html>
```